Retail healthy snack bar design

We are launching a new product range to be sold in health food stores.

The Vorla Co (no logo as yet).

We will have a range of bars, spreads (jars), shakes (bags) in the following ranges-
milk protein
plant protein
keto

For this project, please do a bar design. The chosen designer will be given additional work for the rest of the packaging as well as promotional material such as social media, banners, posters etc.

Brisk Stick Protein - Must be White to be recognized.
Brisk Stick Collagen - Bronze
Brisk Keto Stick - Possibly Red
Brisk Stick Plant - Green

Food images can be added but their must be samples without as we may need to remove for certain countries.

Target Market(s)

Healthy, Weight-loss, Bodybuilding, Elderly, Medical

Industry/Entity Type

Health And Wellness

Font styles to use
Sans Serif

Colors

Designer to choose colors to be used in the design.

Requirements
Must have
• Clean simple to read design with minimal colours

Flavour to be easily read (Must include the word 'Flavour' in the same size font as the flavour description)

Must show size of bar (60g).

Some details that can be added (optional)-
raw, cold pressed bar with (example) whey protein isolate + prebiotic fibre
natural, with no artificial colours, flavours, preservatives or sweeteners
no added sugar or sugar alcohols - gluten free - soy free

Rear of bar shall remain the same or all same details if redesigned.
Nice to have
• Clean design, use of silver foil and/or matt/gloss affect, large oversized flavour image (if including).

See images of current designs I like on the market for ideas
Should not have
• Too many images (if any).

```html
<!DOCTYPE html>
<html lang="en">
<head>
<meta charset="utf-8">
<title>Brisk Stick Protein – Banana Bread bar wrapper</title>
<link rel="stylesheet" href="https://fonts.googleapis.com/css2?family=Source+Sans+3:wght@300;400;600;700&display=swap">
<style>
  :root {
    --bg: #b1b2b4;
    --wrap-blue: #6a84cf;
    --crimp-line: #5b73bd;
    --band-white: #f1f2f4;
    --gold: #d6b446;
    --ink: #1c1a19;
    --mist: #b9bbbe;
    --sans: "Source Sans 3", sans-serif;
  }
  * { margin: 0; padding: 0; box-sizing: border-box; }
  html, body { width: 1200px; height: 1000px; overflow: hidden; }
  body { background: var(--bg); font-family: var(--sans); position: relative; }

  .wrapper {
    position: absolute;
    left: 40px; top: 310px;
    width: 1120px; height: 380px;
  }
  .wrapper-shape { position: absolute; inset: 0; }

  .brand-name {
    position: absolute; left: 170px; top: 8px;
    font-size: 108px; font-weight: 400; letter-spacing: -1px;
    color: var(--gold); white-space: nowrap; line-height: 1;
  }
  .tagline {
    position: absolute; left: 190px; top: 122px;
    font-size: 28px; font-weight: 400; color: var(--gold); white-space: nowrap;
  }
  .flavour-line {
    position: absolute; left: 120px; top: 166px;
    width: 790px; text-align: center;
    font-size: 72px; line-height: 1; white-space: nowrap;
    color: var(--ink); letter-spacing: -0.5px;
  }
  .flavour-line .flavour-name { font-weight: 600; }
  .flavour-line .flavour-word { font-weight: 400; }
  .claims {
    position: absolute; left: 300px; top: 262px;
    font-size: 24px; line-height: 1.15; white-space: nowrap;
  }
  .claims .natural { color: var(--gold); }
  .claims .free-from { color: var(--ink); }
  .claims .no-alcohols { color: var(--mist); font-size: 21px; padding-left: 200px; }

  .net-weight {
    position: absolute; left: 120px; top: 338px;
    font-size: 12px; font-weight: 600; color: var(--gold);
  }
  .online {
    position: absolute; left: 120px; top: 354px;
    font-size: 10px; color: var(--crimp-line); text-transform: uppercase;
  }
  .origin {
    position: absolute; right: 115px; top: 236px;
    font-size: 10px; line-height: 1.2; color: var(--crimp-line); text-align: right;
  }
  .protein-badge {
    position: absolute; right: 118px; top: 178px;
    width: 76px; height: 44px;
    border: 2px solid var(--gold); border-radius: 7px;
    background: var(--wrap-blue);
    display: flex; flex-direction: column; align-items: center; justify-content: center;
    font-size: 11px; font-weight: 600; line-height: 1.1; color: #f3e6b0;
  }
  .protein-badge .badge-protein {
    background: var(--gold); color: #fff; padding: 0 5px; border-radius: 3px; margin-top: 2px;
  }
</style>
</head>
<body>
  <div class="wrapper">
    <svg class="wrapper-shape" width="1120" height="380" viewBox="0 0 1120 380" aria-hidden="true">
      <rect class="wrap-body" x="0" y="0" width="1120" height="380" fill="var(--wrap-blue)"/>
      <polygon class="white-band" points="560,0 1020,0 1020,20 560,380 100,380 100,360" fill="var(--band-white)"/>
      <g class="crimp-left" stroke="var(--crimp-line)" stroke-width="3">
        <line x1="20" y1="0" x2="20" y2="380"/><line x1="36" y1="0" x2="36" y2="380"/>
        <line x1="52" y1="0" x2="52" y2="380"/><line x1="68" y1="0" x2="68" y2="380"/>
        <line x1="84" y1="0" x2="84" y2="380"/>
      </g>
      <g class="crimp-right" stroke="var(--crimp-line)" stroke-width="3">
        <line x1="1036" y1="0" x2="1036" y2="380"/><line x1="1052" y1="0" x2="1052" y2="380"/>
        <line x1="1068" y1="0" x2="1068" y2="380"/><line x1="1084" y1="0" x2="1084" y2="380"/>
        <line x1="1100" y1="0" x2="1100" y2="380"/>
      </g>
    </svg>

    <div class="brand-name">BriskStickProtein</div>
    <div class="tagline">raw, cold pressed whey protein isolate + prebiotic fibre</div>
    <div class="flavour-line"><span class="flavour-name">Banana Bread</span> <span class="flavour-word">Flavour</span></div>

    <div class="claims">
      <div class="natural">natural, with no artificial colours, flavours or preservatives</div>
      <div class="free-from">low fat - low carb - no added sugar - gluten free - soy free</div>
      <div class="no-alcohols">no sugar alcohols</div>
    </div>

    <div class="protein-badge"><span>OVER 20G</span><span class="badge-protein">PROTEIN</span></div>
    <div class="origin">Made in Australia<br>from local ingredients</div>

    <div class="net-weight">NET WT. 2.12 OZ (60g)</div>
    <div class="online">follow us vorlaco online</div>
  </div>
</body>
</html>
```